Launch Invite for LUMEN in hand-drawn chalk style

Looking for an invitation for the launch of LUMEN a creative marketing collaborative founded by Gloria Pembrook. We are a marketing consultancy firm. We are fun, quirky and do things a little different. The launch party will have a silent auction to benefit the charity Guarding Our Prairies. The auction will be a photography show feature local photographers with the theme of Texas natural resources and wildlife. Event will be Wednesday, May 22 from 6:30 to 9:30p at Harlow Gallery located at 514 North 9th, Austin, Texas

Please see the attached verbiage for invite text. Words in bold indicate importance.

We want a chalkboard art invitation similar to the style of Mira Koslowe. So just a black chalkboard background with white chalk text.

http://www.mirakoslowe-example.com/chalk/

Target Market(s)

freinds, family, small business owners, influencers, non-profits

Industry/Entity Type

Charity

Requirements
Must have
• Love the style of the Nora Belden piece on Mira's Website.
Or nagging image or wedding couples image.
chalkboard invite with chalk text
fun, looks like its going to be a good time.
Nice to have
• Highlight lumen, date, time, location, charity

```html
<!DOCTYPE html>
<html lang="en">
<head>
<meta charset="utf-8">
<title>LUMEN Launch Invitation</title>
<link href="https://fonts.googleapis.com/css2?family=Cinzel:wght@400;700&family=Alfa+Slab+One&family=Great+Vibes&family=Pinyon+Script&family=Kalam:wght@400;700&family=Rye&family=IM+Fell+English:ital@0;1&display=swap" rel="stylesheet">
<style>
  :root {
    --board-light: #58aa50;
    --board-mid: #3f9139;
    --board-dark: #2a7229;
    --chalk: #f3f6ef;
    --chalk-soft: rgba(243, 246, 239, 0.8);
    --chalk-haze: rgba(243, 246, 239, 0.16);
  }
  * { margin: 0; padding: 0; box-sizing: border-box; }
  html, body { width: 860px; height: 1200px; overflow: hidden; background: var(--board-dark); }
  .invite {
    position: relative;
    width: 860px;
    height: 1200px;
    background:
      radial-gradient(circle at 30% 25%, rgba(255,255,255,0.05) 0, transparent 180px),
      radial-gradient(circle at 70% 70%, rgba(255,255,255,0.04) 0, transparent 220px),
      radial-gradient(ellipse at 50% 45%, var(--board-light) 0%, var(--board-mid) 55%, var(--board-dark) 100%);
    color: var(--chalk);
    overflow: hidden;
  }
  .chalk-filters { position: absolute; width: 0; height: 0; }
  .chalk-frame { position: absolute; border: 2px solid var(--chalk-soft); filter: url(#chalk-rough); }
  .chalk-frame--outer { inset: 16px; }
  .chalk-frame--inner { inset: 24px; border-width: 1px; }

  .ornament-area {
    position: absolute;
    background: linear-gradient(180deg, rgba(243,246,239,0.30), rgba(243,246,239,0.14));
    border-radius: 6px;
  }
  .ornament-area--name-ribbon { left: 150px; top: 130px; width: 560px; height: 104px; }
  .ornament-area--tagline-scroll { left: 130px; top: 384px; width: 600px; height: 58px; }
  .ornament-area--services-scroll { left: 190px; top: 654px; width: 480px; height: 30px; }
  .ornament-area--date-ribbon { left: 200px; top: 742px; width: 460px; height: 58px; }

  .chalk-text { filter: url(#chalk-rough); text-shadow: 0 0 1.5px rgba(243,246,239,0.7); }
  .line {
    position: absolute;
    left: 0;
    width: 100%;
    text-align: center;
    line-height: 1;
    white-space: nowrap;
  }
  .greeting-hello { top: 36px; font: 400 17px "Cinzel", serif; letter-spacing: 2px; }
  .greeting-city { top: 56px; font: 700 34px "Cinzel", serif; letter-spacing: 1px; }
  .introducing { top: 100px; font: 400 16px "Cinzel", serif; letter-spacing: 2px; }
  .brand-name {
    top: 146px;
    font: 400 74px "Alfa Slab One", serif;
    letter-spacing: 6px;
    color: var(--board-mid);
    -webkit-text-stroke: 2px var(--chalk);
  }
  .founded-by { top: 244px; font: 400 32px "Great Vibes", cursive; }
  .founder { top: 276px; font: 400 46px "Pinyon Script", cursive; }
  .tagline { top: 328px; font: 700 36px "Kalam", cursive; }
  .crafting { top: 484px; font: 400 30px "Kalam", cursive; }
  .services {
    position: absolute;
    top: 534px;
    left: 300px;
    display: grid;
    grid-template-columns: 200px 110px;
    list-style: none;
    font: 400 21px "Kalam", cursive;
    line-height: 27px;
  }
  .celebrate-art { position: absolute; left: 0; top: 680px; width: 860px; height: 90px; }
  .event-date { top: 750px; font: 400 40px "Rye", serif; color: var(--board-dark); text-shadow: none; }
  .event-time { top: 804px; left: 120px; font: 400 18px "Kalam", cursive; }
  .venue { top: 830px; font: 400 33px "IM Fell English", serif; }
  .venue-city { top: 868px; font: 400 31px "IM Fell English", serif; }
  .auction-row {
    position: absolute;
    top: 916px;
    left: 90px;
    right: 90px;
    display: flex;
    justify-content: space-between;
    align-items: center;
    font: italic 400 23px "IM Fell English", serif;
  }
  .auction-star { width: 18px; height: 18px; }
  .cause-note {
    position: absolute;
    top: 962px;
    width: 270px;
    font: 400 19px "Kalam", cursive;
    line-height: 24px;
  }
  .cause-note--left { left: 84px; text-align: right; }
  .cause-note--right { left: 512px; }
  .charity-mark {
    position: absolute;
    left: 368px;
    top: 950px;
    width: 124px;
    height: 124px;
    border: 2px solid var(--chalk);
    border-radius: 50%;
    display: flex;
    align-items: center;
    justify-content: center;
    text-align: center;
    padding: 14px;
    font: 400 19px "Kalam", cursive;
    line-height: 22px;
  }
  .footer-info {
    position: absolute;
    top: 1096px;
    left: 110px;
    right: 110px;
    display: flex;
    justify-content: space-between;
    font: 400 17px "Kalam", cursive;
  }
</style>
</head>
<body>
<main class="invite">
  <svg class="chalk-filters" aria-hidden="true">
    <filter id="chalk-rough" x="-5%" y="-5%" width="110%" height="110%">
      <feTurbulence type="fractalNoise" baseFrequency="0.85" numOctaves="2" seed="4" result="grain"/>
      <feDisplacementMap in="SourceGraphic" in2="grain" scale="2.6" xChannelSelector="R" yChannelSelector="G" result="rough"/>
      <feComponentTransfer in="grain" result="speckle">
        <feFuncA type="table" tableValues="0.55 1 1"/>
      </feComponentTransfer>
      <feComposite in="rough" in2="speckle" operator="in"/>
    </filter>
  </svg>

  <div class="chalk-frame chalk-frame--outer"></div>
  <div class="chalk-frame chalk-frame--inner"></div>

  <div class="ornament-area ornament-area--name-ribbon" role="img" aria-label="Chalk-drawn ribbon banner behind the company name"></div>
  <div class="ornament-area ornament-area--tagline-scroll" role="img" aria-label="Chalk-drawn curled scroll under the tagline"></div>
  <div class="ornament-area ornament-area--services-scroll" role="img" aria-label="Chalk-drawn scroll flourish under the services list"></div>
  <div class="ornament-area ornament-area--date-ribbon" role="img" aria-label="Chalk-drawn ribbon banner carrying the event date"></div>

  <p class="line greeting-hello chalk-text">HELLO</p>
  <p class="line greeting-city chalk-text">AUSTIN!</p>
  <p class="line introducing chalk-text">INTRODUCING</p>
  <h1 class="line brand-name chalk-text">LUMEN</h1>
  <p class="line founded-by chalk-text">founded by</p>
  <p class="line founder chalk-text">Gloria Pembrook</p>
  <p class="line tagline chalk-text">Creative Marketing Collaborative</p>

  <p class="line crafting chalk-text">crafting brands for</p>
  <ul class="services chalk-text">
    <li>small business</li><li>marketing</li>
    <li>non-profits</li><li>strategy</li>
    <li>start ups</li><li>design</li>
    <li>social media</li><li>PR</li>
  </ul>

  <svg class="celebrate-art chalk-text" viewBox="0 680 860 90" fill="none">
    <path id="celebrate-arc" d="M250 760 Q430 700 610 760"/>
    <text font-family="Rye, serif" font-size="50" fill="#f3f6ef" letter-spacing="3" text-anchor="middle">
      <textPath href="#celebrate-arc" startOffset="50%">CELEBRATE</textPath>
    </text>
  </svg>

  <p class="line event-date">Wednesday, May 22</p>
  <p class="line event-time chalk-text">6:30 to 9:30 p.m</p>
  <p class="line venue chalk-text">Harlow Gallery, 514 North 9th</p>
  <p class="line venue-city chalk-text">Austin, Texas</p>

  <div class="auction-row chalk-text">
    <span>Texas Photography Gallery</span>
    <svg class="auction-star" viewBox="0 0 20 20"><path d="M10 1 L12.5 7.5 L19 8 L14 12.5 L15.5 19 L10 15.5 L4.5 19 L6 12.5 L1 8 L7.5 7.5 Z" fill="#f3f6ef"/></svg>
    <span>Silent Auction benefiting</span>
  </div>

  <p class="cause-note cause-note--left chalk-text">Started by Helen Marsh to benefit communities, build on all Texans</p>
  <div class="charity-mark chalk-text">Guarding Our Prairies</div>
  <p class="cause-note cause-note--right chalk-text">to spur conservation efforts that share the success of others, and inspire all to join in.</p>

  <div class="footer-info chalk-text">
    <span>Info: hello@lumengroup-example.com</span>
    <span>Attire: Keep Austin Stylish</span>
  </div>
</main>
</body>
</html>
```